Modern Quillby Tree Care Website

I need a website for a full service Tree Care company. The company provides tree pruning, tree removal, tree preservation, emergency services, stump grinding, and emergency tree services.

Target Market(s)

Customers that need tree services

Industry/Entity Type

Landscaping, Tree Services

Coding

Coded - Design and coding required

Number of Pages Required

5+ page

Font styles to use
Sans Serif

Requirements
Must have
• Good clean design that showcases the services the company provides.
Nice to have
• Services page; contact form, blog, home page, about page

```html
<!DOCTYPE html>
<html lang="en">
<head>
<meta charset="utf-8">
<title>Quillby Tree Care</title>
<link rel="stylesheet" href="https://fonts.googleapis.com/css2?family=Krona+One&family=Montserrat:wght@400;500;600;700&display=swap">
<style>
:root{
  --green:#8dc63f;
  --gold:#e0a93b;
  --tan:#c49a6c;
  --slate:#5f6d6b;
  --ink:#222524;
  --card:#2a2a2a;
  --muted:#b9b9b9;
  --white:#ffffff;
  --footer:#1f2321;
}
*{box-sizing:border-box;margin:0;padding:0}
html,body{width:1200px;height:4800px;overflow:hidden}
body{position:relative;font-family:"Montserrat",sans-serif;color:var(--white);background:var(--white)}
.abs{position:absolute}
.display{font-family:"Krona One",sans-serif;text-transform:uppercase;letter-spacing:1px}
.accent{color:var(--green)}
.gold{color:var(--gold)}
.btn{position:absolute;display:flex;align-items:center;gap:10px;justify-content:center;font-size:13px;font-weight:500;border:1.5px solid var(--green);color:var(--white);background:transparent}
.btn .arrow{width:14px;height:8px}
.photo{position:absolute}

/* header */
.site-header{position:absolute;left:0;top:0;width:1200px;height:70px;z-index:5}
.brand{position:absolute;display:flex;align-items:center;gap:10px;font-family:"Montserrat",sans-serif;font-weight:700;font-size:20px;color:var(--white);white-space:nowrap}
.brand-mark{width:28px;height:28px;background:var(--green)}
.nav{position:absolute;left:436px;top:22px;display:flex;gap:56px;font-size:13px;font-weight:500;text-transform:uppercase}
.nav a{color:var(--white);text-decoration:none}
.nav .current{color:var(--gold);border-bottom:2px solid var(--gold);padding-bottom:3px}
.phone{position:absolute;left:1018px;top:22px;font-size:13px;display:flex;gap:8px;align-items:center}

/* hero */
.hero{position:absolute;left:0;top:0;width:1200px;height:1336px}
.hero-kicker{left:66px;top:198px;font-size:18px;letter-spacing:3px;color:var(--gold);text-transform:uppercase}
.hero-title{left:66px;top:232px;font-size:38px;line-height:56px}
.hero-text{left:66px;top:355px;width:400px;font-size:14px;line-height:24px}
.dots{left:66px;top:606px;display:flex;gap:12px}
.dots span{width:5px;height:5px;border-radius:50%;background:var(--gold)}
.hero-visual{left:520px;top:85px;width:615px;height:615px;background:linear-gradient(160deg,#b58f45 0%,#7d8a3a 50%,#a8a54a 100%)}

/* about */
.about-title{left:560px;top:880px;font-size:27px}
.about-text{left:560px;top:938px;width:580px;font-size:13.5px;line-height:24px;color:#dfe4e2}
.about-text p+p{margin-top:12px}

/* services */
.section-title{position:absolute;left:0;width:1200px;text-align:center;font-size:28px;color:var(--ink)}
.svc-card{position:absolute;width:345px;height:440px;background:var(--card);border-radius:14px}
.svc-card.featured{background:var(--tan)}
.svc-card .img{position:absolute;left:15px;top:15px;width:315px;height:215px;border-radius:6px}
.svc-card h3{position:absolute;left:15px;top:252px;font-size:19px;font-weight:500}
.svc-card h3 span{color:var(--gold)}
.svc-card.featured h3 span{color:var(--white)}
.svc-card p{position:absolute;left:15px;top:290px;width:300px;font-size:12.5px;line-height:22px;color:var(--muted)}
.svc-card.featured p{color:#fff2e0}
.svc-card .btn{left:15px;top:375px;width:138px;height:42px}
.svc-card.featured .btn{background:var(--white);color:var(--ink);border-color:var(--white)}
.view-all{position:absolute;left:512px;top:2436px;width:176px;height:46px;background:var(--slate);color:var(--white);font-size:12px;font-weight:600;display:flex;align-items:center;justify-content:center}

/* contact */
.field{position:absolute;background:var(--white);color:#888;font-size:12px;padding:10px 8px}
.submit{position:absolute;border:1.5px solid var(--green);color:var(--white);font-size:13px;display:flex;align-items:center;justify-content:center}

/* blog */
.blog-card{position:absolute;width:345px;height:418px;background:var(--card);border-radius:14px}
.blog-card .img{position:absolute;left:15px;top:15px;width:315px;height:200px;border-radius:6px}
.date-badge{position:absolute;left:28px;top:200px;width:34px;height:30px;background:var(--gold);font-weight:700;font-size:15px;display:flex;align-items:center;justify-content:center}
.date-text{position:absolute;left:66px;top:218px;font-size:10.5px}
.blog-card h3{position:absolute;left:15px;top:260px;width:320px;font-size:19px;font-weight:500;line-height:28px}
.blog-card .btn{left:15px;top:342px;width:138px;height:42px}

/* why choose */
.why-title{left:66px;top:3880px;font-size:26px}
.why-text{left:66px;top:3944px;width:470px;font-size:14px;line-height:26px;color:#c8cdca}
.checks{left:66px;top:4025px;list-style:none}
.checks li{display:flex;align-items:center;gap:10px;font-size:13px;font-weight:500;height:38px}
.checks svg{width:24px;height:24px}

/* footer */
.footer{position:absolute;left:0;top:4350px;width:1200px;height:450px;background:var(--footer)}
.foot-h{position:absolute;font-size:19px;font-weight:500;color:var(--gold);text-transform:uppercase}
.foot-links{position:absolute;list-style:none;font-size:13px;color:#d5d5d5}
.foot-links li{height:34px}
.foot-nav{position:absolute;left:0;width:1200px;top:184px;text-align:center;font-size:11.5px;color:#d5d5d5;letter-spacing:.5px}
.follow{position:absolute;left:0;width:1200px;top:230px;text-align:center;font-size:15px;font-weight:500}
.socials{position:absolute;left:490px;top:268px;display:flex;gap:12px}
.socials span{width:34px;height:34px;background:var(--white)}
.socials span.on{background:#8a9a9a}
.contact-row{position:absolute;left:880px;display:flex;gap:16px;font-size:13px;line-height:21px;color:#d5d5d5}
.contact-row svg{width:18px;height:18px;flex:none;margin-top:2px}
.foot-bar{position:absolute;left:66px;top:390px;width:1068px;border-top:1px solid #3a3f3c}
.legal{position:absolute;left:66px;top:405px;font-size:10px;color:#cfcfcf}
.copy{position:absolute;left:0;width:1200px;top:403px;text-align:center;font-size:12px;color:#d5d5d5}
</style>
</head>
<body>

<!-- HERO + ABOUT -->
<section class="hero">
  <svg class="abs" width="1200" height="1336" viewBox="0 0 1200 1336">
    <defs>
      <linearGradient id="heroBg" x1="0" y1="0" x2="1" y2="1">
        <stop offset="0" stop-color="#2b332d"/>
        <stop offset="1" stop-color="#1c221e"/>
      </linearGradient>
    </defs>
    <rect width="1200" height="1336" fill="var(--slate)"/>
    <polygon points="0,0 1200,0 1200,700 0,640" fill="url(#heroBg)" role="img" aria-label="Dark forest background behind the header"/>
  </svg>
  <div class="abs hero-visual" role="img" aria-label="Hero photo of an arborist with a chainsaw cutting a log"></div>

  <header class="site-header">
    <div class="brand" style="left:66px;top:14px"><span class="brand-mark"></span>Quillby Tree Care</div>
    <nav class="nav">
      <a class="current" href="#">Home</a><a href="#">About Us</a><a href="#">Services</a><a href="#">Blog</a><a href="#">Contact Us</a>
    </nav>
    <div class="phone">
      <svg width="12" height="14" viewBox="0 0 12 14"><path d="M2 1l3 0 1 3-2 1.5q1.5 3 4 4.5L9.5 8l2.5 1v3l-1.5 1.5Q3 12 .5 2.5z" fill="var(--gold)"/></svg>
      (555) 204-8817
    </div>
  </header>

  <div class="abs hero-kicker">Quillby for</div>
  <h1 class="abs display hero-title">All your <span class="accent">tree care</span><br>needs</h1>
  <p class="abs hero-text">Duis aute irure dolor in reprehenderit in voluptate velit esse cillum dolore eu fugiat</p>
  <a class="btn" style="left:66px;top:432px;width:178px;height:46px">Request A Quote
    <svg class="arrow" viewBox="0 0 14 8"><path d="M0 4h12M9 1l3 3-3 3" stroke="#fff" fill="none" stroke-width="1.3"/></svg></a>
  <div class="abs dots"><span></span><span></span><span></span></div>

  <svg class="abs" style="left:58px;top:790px" width="478" height="476" viewBox="0 0 478 476">
    <path d="M5 470 V170 A165 165 0 0 1 170 5 H300 A165 165 0 0 1 465 170 V470" fill="none" stroke="#fff" stroke-width="3"/>
    <path d="M12 465 V178 A158 158 0 0 1 170 20 H300 A158 158 0 0 1 458 178 V465 Z" fill="#7f7a3e" role="img" aria-label="Worker cutting a log with a chainsaw in an orchard"/>
    <path d="M280 470 H470 V390" fill="none" stroke="#fff" stroke-width="4"/>
  </svg>
  <h2 class="abs display about-title">Who we <span class="accent">are</span></h2>
  <div class="abs about-text">
    <p>At Quillby Tree Care, we are more than just a tree service company, we are stewards of our beautiful trees. With a passion deeply rooted in arboriculture, we embark on a mission to promote the health, beauty, and safety of your trees and landscapes.</p>
    <p>Whether it's expert tree trimming to enhance aesthetics, meticulous tree removal to mitigate hazards, or comprehensive tree health assessments to ensure safety, we approach each task with unwavering dedication and attention to detail.</p>
  </div>
  <a class="btn" style="left:560px;top:1128px;width:136px;height:42px">Read More
    <svg class="arrow" viewBox="0 0 14 8"><path d="M0 4h12M9 1l3 3-3 3" stroke="#fff" fill="none" stroke-width="1.3"/></svg></a>
</section>

<!-- SERVICES -->
<section>
  <h2 class="section-title display" style="top:1430px">Our <span class="accent">services</span></h2>

  <article class="svc-card featured" style="left:66px;top:1495px">
    <div class="img" style="background:linear-gradient(135deg,#3f6b2c,#7a3b3b)" role="img" aria-label="Man trimming a hedge with shears"></div>
    <h3><span>Tree</span> Trimming</h3>
    <p>Sed ut perspiciatis unde omnis iste natus error sit voluptatem accusantium doloremque laudantium</p>
    <a class="btn">Read More <svg class="arrow" viewBox="0 0 14 8"><path d="M0 4h12M9 1l3 3-3 3" stroke="#222" fill="none" stroke-width="1.3"/></svg></a>
  </article>
  <article class="svc-card" style="left:427px;top:1495px">
    <div class="img" style="background:linear-gradient(135deg,#8f8f8f,#3f4a40)" role="img" aria-label="Climber cutting a tree trunk with a chainsaw"></div>
    <h3><span>Tree</span> Removal</h3>
    <p>Sed ut perspiciatis unde omnis iste natus error sit voluptatem accusantium doloremque laudantium</p>
    <a class="btn">Read More <svg class="arrow" viewBox="0 0 14 8"><path d="M0 4h12M9 1l3 3-3 3" stroke="#fff" fill="none" stroke-width="1.3"/></svg></a>
  </article>
  <article class="svc-card" style="left:788px;top:1495px">
    <div class="img" style="background:linear-gradient(180deg,#9fb4c2,#5b6a3a)" role="img" aria-label="Workers clearing land with shovels"></div>
    <h3><span>Tree</span> Clearing</h3>
    <p>Sed ut perspiciatis unde omnis iste natus error sit voluptatem accusantium doloremque laudantium</p>
    <a class="btn">Read More <svg class="arrow" viewBox="0 0 14 8"><path d="M0 4h12M9 1l3 3-3 3" stroke="#fff" fill="none" stroke-width="1.3"/></svg></a>
  </article>
  <article class="svc-card" style="left:66px;top:1952px">
    <div class="img" style="background:linear-gradient(135deg,#9aa98a,#5c7a3c)" role="img" aria-label="Worker pruning branches with a pole saw"></div>
    <h3><span>Tree</span> Pruning</h3>
    <p>Sed ut perspiciatis unde omnis iste natus error sit voluptatem accusantium doloremque laudantium</p>
    <a class="btn">Read More <svg class="arrow" viewBox="0 0 14 8"><path d="M0 4h12M9 1l3 3-3 3" stroke="#fff" fill="none" stroke-width="1.3"/></svg></a>
  </article>
  <article class="svc-card" style="left:427px;top:1952px">
    <div class="img" style="background:linear-gradient(135deg,#c9602e,#6e5a44)" role="img" aria-label="Log on a sawmill machine"></div>
    <h3><span>Stump</span> Grinding</h3>
    <p>Sed ut perspiciatis unde omnis iste natus error sit voluptatem accusantium doloremque laudantium</p>
    <a class="btn">Read More <svg class="arrow" viewBox="0 0 14 8"><path d="M0 4h12M9 1l3 3-3 3" stroke="#fff" fill="none" stroke-width="1.3"/></svg></a>
  </article>
  <article class="svc-card" style="left:788px;top:1952px">
    <div class="img" style="background:linear-gradient(135deg,#8aa05a,#4e5b3a)" role="img" aria-label="Volunteers planting a young tree"></div>
    <h3><span>Tree</span> Preservation</h3>
    <p>Sed ut perspiciatis unde omnis iste natus error sit voluptatem accusantium doloremque laudantium</p>
    <a class="btn">Read More <svg class="arrow" viewBox="0 0 14 8"><path d="M0 4h12M9 1l3 3-3 3" stroke="#fff" fill="none" stroke-width="1.3"/></svg></a>
  </article>

  <a class="view-all">VIEW ALL SERVICES</a>
</section>

<!-- CONTACT -->
<section>
  <svg class="abs" style="left:0;top:2580px" width="1200" height="560" viewBox="0 0 1200 560">
    <defs>
      <linearGradient id="contactBg" x1="0" y1="0" x2="1" y2="0">
        <stop offset="0" stop-color="#2d3a2c"/><stop offset="1" stop-color="#3b4a36"/>
      </linearGradient>
      <linearGradient id="contactPhoto" x1="0" y1="0" x2="1" y2="1">
        <stop offset="0" stop-color="#6e6a4f"/><stop offset=".5" stop-color="#b9754a"/><stop offset="1" stop-color="#d8b57c"/>
      </linearGradient>
    </defs>
    <polygon points="0,0 1200,0 1200,440 0,560" fill="url(#contactBg)" role="img" aria-label="Dark forest floor background"/>
    <polygon points="620,0 1200,0 1200,440 620,506" fill="url(#contactPhoto)" role="img" aria-label="Arborist in safety gear cutting a tree trunk"/>
  </svg>
  <div class="abs" style="left:66px;top:2670px;font-size:16px;color:var(--gold);text-transform:uppercase">Contact us</div>
  <h2 class="abs display" style="left:66px;top:2710px;font-size:28px;line-height:46px">If you have any<br><span class="accent">question</span></h2>
  <div class="field" style="left:66px;top:2822px;width:237px;height:40px">Name:</div>
  <div class="field" style="left:311px;top:2822px;width:237px;height:40px">Email:</div>
  <div class="field" style="left:66px;top:2872px;width:237px;height:40px">Phone:</div>
  <div class="field" style="left:311px;top:2872px;width:237px;height:90px">Message:</div>
  <div class="submit" style="left:66px;top:2922px;width:237px;height:40px">Submit</div>
</section>

<!-- BLOG -->
<section>
  <h2 class="section-title display" style="top:3180px">Recent <span class="accent">blog</span></h2>

  <article class="blog-card" style="left:66px;top:3245px">
    <div class="img" style="background:linear-gradient(135deg,#5d7a3c,#c9d26a)" role="img" aria-label="Two foresters measuring a tree with tape"></div>
    <div class="date-badge">23</div><div class="date-text">MAY, 2024</div>
    <h3>Reprehenderit qui in ea voluptate velit esse quam nihil</h3>
    <a class="btn">Read More <svg class="arrow" viewBox="0 0 14 8"><path d="M0 4h12M9 1l3 3-3 3" stroke="#fff" fill="none" stroke-width="1.3"/></svg></a>
  </article>
  <article class="blog-card" style="left:427px;top:3245px">
    <div class="img" style="background:linear-gradient(135deg,#4a4238,#a58d6b)" role="img" aria-label="Logger cutting fallen logs with a chainsaw"></div>
    <div class="date-badge">15</div><div class="date-text">MAY, 2024</div>
    <h3>Reprehenderit qui in ea voluptate velit esse quam nihil</h3>
    <a class="btn">Read More <svg class="arrow" viewBox="0 0 14 8"><path d="M0 4h12M9 1l3 3-3 3" stroke="#fff" fill="none" stroke-width="1.3"/></svg></a>
  </article>
  <article class="blog-card" style="left:788px;top:3245px">
    <div class="img" style="background:linear-gradient(135deg,#6a6b52,#3f4532)" role="img" aria-label="Forester standing by a stump in the woods"></div>
    <div class="date-badge">12</div><div class="date-text">APRIL, 2024</div>
    <h3>Reprehenderit qui in ea voluptate velit esse quam nihil</h3>
    <a class="btn">Read More <svg class="arrow" viewBox="0 0 14 8"><path d="M0 4h12M9 1l3 3-3 3" stroke="#fff" fill="none" stroke-width="1.3"/></svg></a>
  </article>
</section>

<!-- WHY CHOOSE US -->
<section>
  <svg class="abs" style="left:0;top:3720px" width="1200" height="630" viewBox="0 0 1200 630">
    <polygon points="0,0 1200,127 1200,630 0,630" fill="#26302d" role="img" aria-label="Dark forest background"/>
  </svg>
  <h2 class="abs display why-title">Why choose <span class="accent">us</span></h2>
  <p class="abs why-text">Sed ut perspiciatis unde omnis iste natus error sit voluptatem accusantium doloremque laudantium</p>
  <ul class="abs checks">
    <li><svg viewBox="0 0 24 24"><circle cx="12" cy="12" r="10.5" fill="none" stroke="var(--green)" stroke-width="1.5"/><path d="M7 12l3.5 3.5L17 9" fill="none" stroke="var(--green)" stroke-width="2"/></svg>Licensed and Insured</li>
    <li><svg viewBox="0 0 24 24"><circle cx="12" cy="12" r="10.5" fill="none" stroke="var(--green)" stroke-width="1.5"/><path d="M7 12l3.5 3.5L17 9" fill="none" stroke="var(--green)" stroke-width="2"/></svg>24 Hours Emergency Services</li>
    <li><svg viewBox="0 0 24 24"><circle cx="12" cy="12" r="10.5" fill="none" stroke="var(--green)" stroke-width="1.5"/><path d="M7 12l3.5 3.5L17 9" fill="none" stroke="var(--green)" stroke-width="2"/></svg>Locally Owned &amp; Operated</li>
    <li><svg viewBox="0 0 24 24"><circle cx="12" cy="12" r="10.5" fill="none" stroke="var(--green)" stroke-width="1.5"/><path d="M7 12l3.5 3.5L17 9" fill="none" stroke="var(--green)" stroke-width="2"/></svg>Professionl Work</li>
    <li><svg viewBox="0 0 24 24"><circle cx="12" cy="12" r="10.5" fill="none" stroke="var(--green)" stroke-width="1.5"/><path d="M7 12l3.5 3.5L17 9" fill="none" stroke="var(--green)" stroke-width="2"/></svg>Safety is Our No 1 priority</li>
    <li><svg viewBox="0 0 24 24"><circle cx="12" cy="12" r="10.5" fill="none" stroke="var(--green)" stroke-width="1.5"/><path d="M7 12l3.5 3.5L17 9" fill="none" stroke="var(--green)" stroke-width="2"/></svg>Free Estimate</li>
    <li><svg viewBox="0 0 24 24"><circle cx="12" cy="12" r="10.5" fill="none" stroke="var(--green)" stroke-width="1.5"/><path d="M7 12l3.5 3.5L17 9" fill="none" stroke="var(--green)" stroke-width="2"/></svg>Licensed Arborist on Staff</li>
  </ul>
  <div class="photo" style="left:605px;top:3885px;width:517px;height:400px;background:linear-gradient(160deg,#6f9fd0 0%,#4d6a3a 45%,#b09068 100%)" role="img" aria-label="Chainsaw resting on a cut log in a clearing"></div>
  <div class="photo" style="left:585px;top:3875px;width:135px;height:130px;background:linear-gradient(135deg,#8a6a58,#c7a58c);border:3px solid #fff" role="img" aria-label="Pile of cut log rounds"></div>
  <div class="photo" style="left:1005px;top:4180px;width:117px;height:110px;background:linear-gradient(135deg,#6c7d4b,#3c4a34);border:3px solid #fff" role="img" aria-label="Worker cutting a tree in the woods"></div>
</section>

<!-- FOOTER -->
<footer class="footer">
  <div class="foot-h" style="left:66px;top:78px">Services</div>
  <ul class="foot-links" style="left:66px;top:124px">
    <li>Tree Pruning</li><li>Tree Removal</li><li>Tree Preservation</li><li>Emergency Services</li><li>Stump Grinding</li><li>Emergency Tree Services</li>
  </ul>

  <div class="brand" style="left:478px;top:95px;font-size:26px"><span class="brand-mark" style="width:34px;height:34px"></span>Quillby Tree Care</div>
  <div class="foot-nav">HOME &nbsp;|&nbsp; ABOUT US &nbsp;|&nbsp; SERVICES &nbsp;|&nbsp; BLOG &nbsp;|&nbsp; CONTACT US</div>
  <div class="follow">FOLLOW US</div>
  <div class="socials" aria-label="Social links">
    <span></span><span class="on"></span><span></span><span></span><span></span>
  </div>

  <div class="foot-h" style="left:880px;top:78px">Contacts</div>
  <div class="contact-row" style="top:124px">
    <svg viewBox="0 0 18 18"><path d="M9 1a5.5 5.5 0 0 0-5.5 5.5C3.5 11 9 17 9 17s5.5-6 5.5-10.5A5.5 5.5 0 0 0 9 1z" fill="var(--gold)"/><circle cx="9" cy="6.5" r="2" fill="var(--footer)"/></svg>
    <span>14 Hollow Oak Lane<br>Brindlewood 40KA USA</span>
  </div>
  <div class="contact-row" style="top:196px">
    <svg viewBox="0 0 18 18"><path d="M3 2h4l1.5 4-2.5 2q2 4 5 5.5l2-2.5 4 1.5v4l-2 1.5Q4 16 1.5 4z" fill="none" stroke="var(--gold)" stroke-width="1.3"/></svg>
    <span>(555) 204-8817 / (555) 310-4462</span>
  </div>
  <div class="contact-row" style="top:250px">
    <svg viewBox="0 0 18 18"><rect x="1.5" y="3.5" width="15" height="11" fill="var(--gold)"/><path d="M1.5 3.5L9 10l7.5-6.5" fill="none" stroke="var(--footer)" stroke-width="1.3"/></svg>
    <span>hello@quillbytreecare.com</span>
  </div>

  <div class="foot-bar"></div>
  <div class="legal">Terms &amp; Condition &nbsp;|&nbsp; Privacy Policy</div>
  <div class="copy">© <span class="gold">Quillby Tree Care</span>, 2024. All Rights Reserved.</div>
</footer>

</body>
</html>
```